BAKF Donor Grab brochure design needed

Bright Anchor Kinship Foundation (BAKF) needs brochure (or other marketing piece) that will compel those who see it to read it and activate them donate and support the organization and the Veterans and families it serves. The Bright Anchor Kinship Foundation is a non-profit 501c3 charitable entity that exists for the express purpose of addressing systemic inequities regarding access to and excellence in care provided by the Office of Harbor Affairs, Pioneer’s Care Directorate of Civilian Healthcare Facilities to Veterans and their families. Here is the URL link to the website where txt can be found: www.mybakf.org

Target Market(s)

all ethnicities, patriots, corporate America, other charitable organizations, individual and group donors

Industry/Entity Type

Health and wellness

Other font styles liked:
• Ariel

Requirements
Must have
• excitement, must be compelling, tell a story

```html
<!DOCTYPE html>
<html lang="en">
<head>
<meta charset="utf-8">
<title>Bright Anchor Kinship Foundation – Donor Brochure</title>
<link href="https://fonts.googleapis.com/css2?family=Montserrat:wght@500;600;700;800&family=Open+Sans:wght@400;600;700&display=swap" rel="stylesheet">
<style>
  :root{
    --teal:#1e8c74;
    --teal-dark:#136a58;
    --teal-light:#3aa88c;
    --green:#2f6f3e;
    --ink:#4b4f52;
    --paper:#ffffff;
    --paper-shade:#e6e9e8;
    --canvas:#d9dbdb;
    --photo-warm:#a58d6a;
    --photo-green:#6f8f4c;
    --photo-clinic:#c9c6c0;
  }
  *{box-sizing:border-box;margin:0;padding:0}
  html,body{width:691px;height:1200px;overflow:hidden;background:var(--canvas)}
  body{position:relative;font-family:"Open Sans",Arial,sans-serif;color:var(--ink)}
  .page{position:absolute;overflow:hidden;background:linear-gradient(160deg,var(--paper) 40%,var(--paper-shade));box-shadow:0 3px 10px rgba(0,0,0,.25)}
  .fill{position:absolute;inset:0;width:100%;height:100%}
  .abs{position:absolute}
  .heading{font-family:"Montserrat",Arial,sans-serif;font-weight:700;text-transform:uppercase;color:var(--teal)}
  .small{font-size:5.2px;line-height:1.45}
  .spread-fold{position:absolute;top:0;bottom:0;left:50%;width:24px;margin-left:-12px;background:linear-gradient(90deg,transparent,rgba(0,0,0,.12) 50%,transparent);pointer-events:none}

  /* cover */
  .cover{left:75.5px;top:91px;width:540px;height:380px}
  .cover-tagline{left:38px;top:300px;width:250px;font-family:"Montserrat",Arial,sans-serif;font-weight:700;font-size:13.5px;line-height:1.25;color:#fff;letter-spacing:.6px}
  .cover-url{left:38px;top:352px;font-size:12px;color:#fff;letter-spacing:.5px;display:flex;align-items:center;gap:6px}
  .cover-url .dot{width:9px;height:9px;border:1.5px solid #fff;border-radius:50%}
  .donate-badge{border-radius:50%;background:#2f9fd6;border:3px solid #e8f6fc;color:#fff;font-family:"Montserrat",Arial,sans-serif;font-weight:800;display:flex;align-items:center;justify-content:center;letter-spacing:.5px}
  .cover .donate-badge{left:30px;top:236px;width:66px;height:66px;font-size:12px}
  .brand{display:flex;align-items:center;gap:8px}
  .brand-mark{width:22px;height:22px;border-radius:50%;background:var(--green)}
  .brand-name{font-family:"Montserrat",Arial,sans-serif;font-weight:700;color:var(--green);text-transform:uppercase;line-height:1.1}
  .cover .brand{left:330px;top:292px}
  .cover .brand-name{font-size:12.5px;width:170px}

  /* spreads */
  .spread{position:absolute;left:25.5px;width:640px;height:228px}
  .spread .page{top:0;width:320px;height:228px}
  .spread .page.left{left:0}
  .spread .page.right{left:320px}
  .spread-one{top:562px}
  .spread-two{top:881px}

  .story{left:138px;top:20px;width:170px}
  .story .heading{font-size:8px;color:var(--green);margin-bottom:5px}
  .story-item{display:flex;gap:7px;margin-bottom:6px}
  .story-icon{flex:none;width:20px;height:20px;border-radius:50%;background:var(--teal)}
  .story-item h4{font-family:"Montserrat",Arial,sans-serif;font-size:5.6px;color:var(--green);text-transform:uppercase}
  .story-item ol{padding-left:7px}

  .forum-lines{left:10px;top:13px;width:300px;text-align:center;color:#fff;font-family:"Montserrat",Arial,sans-serif;font-weight:600;font-size:6.2px;line-height:1.4;letter-spacing:.2px;white-space:nowrap}
  .photo-row{left:18px;top:62px;display:flex;gap:6px}
  .photo-row svg{width:90px;height:62px;border:2px solid #fff;box-shadow:0 1px 3px rgba(0,0,0,.3)}
  .mission-block{left:22px;top:134px;width:280px}
  .mission-block .heading{font-size:7.5px;color:var(--green);text-align:center;margin-bottom:5px}
  .tick-list{list-style:none}
  .tick-list li{display:flex;gap:4px;margin-bottom:3px}
  .tick{flex:none;width:6px;height:6px;border:1px solid var(--teal);border-radius:50%;position:relative;margin-top:.5px}
  .tick::after{content:"";position:absolute;left:1.3px;top:.4px;width:1.5px;height:2.6px;border:solid var(--teal);border-width:0 .8px .8px 0;transform:rotate(45deg)}
  .join-line{display:flex;align-items:center;gap:8px;margin-top:4px;font-size:5.2px;line-height:1.4;color:var(--green)}
  .join-line .join-text{flex:1 1 auto;min-width:0}
  .url-pill{flex:none;white-space:nowrap;background:var(--green);color:#fff;font-size:7px;padding:2px 16px;border-radius:8px}

  .care-heading{left:30px;top:128px;width:270px;text-align:center}
  .care-heading .heading{font-size:7.5px;color:var(--green)}
  .care-heading .small{font-size:5.2px;color:var(--teal)}
  .care-text{left:30px;top:158px;width:195px}
  .care-box{left:0;top:185px;width:320px;height:43px}
  .care-box-text{left:40px;top:195px;width:160px;color:#fff}
  .spread-two .donate-badge{left:242px;top:163px;width:40px;height:40px;font-size:7px;border-width:2px}

  .about{left:18px;top:18px;width:150px}
  .about h3{display:flex;align-items:center;gap:4px;font-family:"Montserrat",Arial,sans-serif;font-size:7px;color:var(--green);text-transform:uppercase;margin-bottom:3px}
  .about h3 .bullet{width:8px;height:8px;border-radius:50%;background:var(--green)}
  .about p{margin-bottom:4px}
  .about .mission{margin-top:12px}
</style>
</head>
<body>

<!-- Cover -->
<section class="page cover" aria-label="Brochure cover">
  <svg class="fill" viewBox="0 0 540 380" preserveAspectRatio="none" role="img" aria-label="Photograph of a smiling family of four seated together on a sunny lawn">
    <defs>
      <linearGradient id="coverPhoto" x1="0" y1="0" x2="1" y2="1">
        <stop offset="0" stop-color="#b9a785"/>
        <stop offset=".5" stop-color="var(--photo-warm)"/>
        <stop offset="1" stop-color="var(--photo-green)"/>
      </linearGradient>
    </defs>
    <path d="M0 0H540V190Q420 245 270 272Q130 292 0 288Z" fill="url(#coverPhoto)"/>
  </svg>
  <svg class="fill" viewBox="0 0 540 380" preserveAspectRatio="none" aria-hidden="true">
    <defs>
      <linearGradient id="coverBand" x1="0" y1="0" x2="1" y2="0">
        <stop offset="0" stop-color="var(--teal-dark)"/>
        <stop offset="1" stop-color="var(--teal-light)"/>
      </linearGradient>
    </defs>
    <path d="M0 288Q130 292 270 272Q420 245 540 190V198Q420 255 270 282Q130 302 0 298Z" fill="#d8dcdb"/>
    <path d="M0 292Q170 298 330 262Q300 330 250 380H0Z" fill="url(#coverBand)"/>
  </svg>
  <div class="abs donate-badge">DONATE</div>
  <p class="abs cover-tagline">…HEALTHY AND WELL LIVES UNDIMINISHED BY SERVICE RELATED HEALTH CONCERNS…</p>
  <p class="abs cover-url"><span class="dot"></span>www.mybakf.org</p>
  <div class="abs brand">
    <span class="brand-mark"></span>
    <span class="brand-name">Bright Anchor Kinship Foundation</span>
  </div>
</section>

<!-- Spread one -->
<section class="spread spread-one" aria-label="Our story and support our mission spread">
  <div class="page left">
    <svg class="fill" viewBox="0 0 320 228" preserveAspectRatio="none" role="img" aria-label="Photograph of uniformed service members talking outdoors">
      <defs>
        <linearGradient id="storyPhoto" x1="0" y1="0" x2="1" y2="1">
          <stop offset="0" stop-color="#5f7d48"/>
          <stop offset=".6" stop-color="#a89676"/>
          <stop offset="1" stop-color="#7d8a6a"/>
        </linearGradient>
      </defs>
      <path d="M0 20Q60 8 120 0V0Q100 80 125 228H0Z" fill="url(#storyPhoto)"/>
    </svg>
    <svg class="fill" viewBox="0 0 320 228" preserveAspectRatio="none" aria-hidden="true">
      <path d="M0 0H180Q90 5 0 40Z" fill="var(--teal)"/>
    </svg>
    <div class="abs story">
      <h2 class="heading">Our Story</h2>
      <div class="story-item"><span class="story-icon"></span><div class="small"><h4>Purpose</h4>Make good on a promise "To care for those who shall have borne the battle" (adapted from Elias Thornbury).</div></div>
      <div class="story-item"><span class="story-icon"></span><div class="small"><h4>Vision</h4>BAKF envisions a world in which ALL veterans and their families live healthy and well lives undiminished by service related health concerns.</div></div>
      <div class="story-item"><span class="story-icon"></span><div class="small"><h4>Strategy</h4>
        <ol>
          <li>Amplify the veteran community voice in their battle for health and wellness.</li>
          <li>Facilitate equitable healthcare for veterans and families.</li>
          <li>Develop and share health education in the communities where they live.</li>
          <li>Implement training that deepens care for veterans.</li>
          <li>Refine the Kinship Care Circle model.</li>
        </ol></div></div>
    </div>
    <div class="spread-fold" style="left:100%"></div>
  </div>
  <div class="page right">
    <svg class="fill" viewBox="0 0 320 228" preserveAspectRatio="none" aria-hidden="true">
      <defs>
        <linearGradient id="forumBand" x1="0" y1="0" x2="1" y2="0">
          <stop offset="0" stop-color="var(--teal-light)"/>
          <stop offset="1" stop-color="var(--teal-dark)"/>
        </linearGradient>
      </defs>
      <path d="M0 0H320V44Q240 58 120 60Q50 62 0 60Z" fill="url(#forumBand)"/>
    </svg>
    <p class="abs forum-lines">HEALTHCARE EDUCATION AND TRAINING<br>COMMUNITY HEALTH AND WELLNESS ENGAGEMENT EVENTS<br>HEALTH AND WELLNESS EDUCATION FORUMS</p>
    <div class="abs photo-row">
      <svg viewBox="0 0 90 62" preserveAspectRatio="none" role="img" aria-label="Photograph of veterans in uniform standing together"><rect width="90" height="62" fill="#7e8a7a"/></svg>
      <svg viewBox="0 0 90 62" preserveAspectRatio="none" role="img" aria-label="Photograph of sailors in white uniforms at attention"><rect width="90" height="62" fill="#9aa3a6"/></svg>
      <svg viewBox="0 0 90 62" preserveAspectRatio="none" role="img" aria-label="Photograph of a family sitting together indoors"><rect width="90" height="62" fill="#c8b8a6"/></svg>
    </div>
    <div class="abs mission-block">
      <h2 class="heading">Support Our Mission</h2>
      <ul class="tick-list small">
        <li><span class="tick"></span>20 million discharged American warriors are either currently suffering multiple chronic conditions or are at risk.</li>
        <li><span class="tick"></span>42 million family members are also affected.</li>
        <li><span class="tick"></span>62 million total number of those needing some form of specialized care.</li>
        <li><span class="tick"></span>These 62 million Americans represent about 17% of the entire U.S. population.</li>
      </ul>
      <div class="join-line"><span class="join-text">Join Forces with the Foundation and be a CHAMPION for our Heroes and their Families</span><span class="url-pill">www.mybakf.org</span></div>
    </div>
  </div>
</section>

<!-- Spread two -->
<section class="spread spread-two" aria-label="Quality care and who we are spread">
  <div class="page left">
    <svg class="fill" viewBox="0 0 320 228" preserveAspectRatio="none" role="img" aria-label="Photograph of a nurse with a mother and young daughter in a clinic">
      <defs>
        <linearGradient id="clinicPhoto" x1="0" y1="0" x2="1" y2="0">
          <stop offset="0" stop-color="var(--photo-clinic)"/>
          <stop offset=".5" stop-color="#8d7f78"/>
          <stop offset="1" stop-color="#d7d3cd"/>
        </linearGradient>
      </defs>
      <path d="M0 0H320V90Q180 100 0 125Z" fill="url(#clinicPhoto)"/>
    </svg>
    <svg class="fill" viewBox="0 0 320 228" preserveAspectRatio="none" aria-hidden="true">
      <path d="M0 125Q180 100 320 90V94Q180 104 0 129Z" fill="var(--teal)"/>
      <path d="M0 190Q160 184 320 176V228H0Z" fill="var(--teal)"/>
    </svg>
    <div class="abs care-heading">
      <h2 class="heading">Quality Care for Children of Veterans</h2>
      <p class="small">Military children have more healthcare needs, but less access and lower quality</p>
    </div>
    <p class="abs care-text small">Children in military families insured by HarborCare are more likely to have special health care needs, and more likely to have a behavioral health diagnosis compared to their civilian peers.</p>
    <p class="abs care-box-text small">Veteran families are also affected. This brings the number of those needing specialized care to 62 million, about 17% of the U.S. population.</p>
    <div class="abs donate-badge">DONATE</div>
    <div class="spread-fold" style="left:100%"></div>
  </div>
  <div class="page right">
    <svg class="fill" viewBox="0 0 320 228" preserveAspectRatio="none" role="img" aria-label="Photograph of a family walking outdoors with a child on a parent's shoulders">
      <defs>
        <linearGradient id="walkPhoto" x1="0" y1="0" x2="1" y2="1">
          <stop offset="0" stop-color="#b7b8ad"/>
          <stop offset="1" stop-color="#6d6a5d"/>
        </linearGradient>
      </defs>
      <path d="M320 0V228H195Q160 120 190 30Q220 10 320 0Z" fill="url(#walkPhoto)"/>
    </svg>
    <svg class="fill" viewBox="0 0 320 228" preserveAspectRatio="none" aria-hidden="true">
      <path d="M200 0H320V0Q300 12 260 20Q220 25 200 0Z" fill="var(--teal)"/>
    </svg>
    <div class="abs about small">
      <h3><span class="bullet"></span>Who We Are</h3>
      <p>Having devoted their lives to serving our country, veterans leave military service with a host of debilitating health conditions, many remaining unknown for years after discharge. The Bright Anchor Kinship Foundation (BAKF), a non-profit 501c3 charitable entity, was established to address systemic inequities in access to and quality of care.</p>
      <p>BAKF works tirelessly so veterans and their families are connected, educated and trained to access integrated healthcare and community support.</p>
      <h3 class="mission"><span class="bullet"></span>Our Mission</h3>
      <p>The foundation is committed to helping and giving back to the men, women and families who serve our nation, whether in uniform or not, at home or abroad.</p>
      <p>Join forces with BAKF to give the words "Thank You for Your Service" real meaning.</p>
    </div>
  </div>
</section>

</body>
</html>
```